依頼詳細
PCとスマホデザインの両方納品をいただきますが、
まずはデザインイメージが確認しやすいPCページのみの提案をお願いします。
スマホページは当選者に納品時にお願いしたいと思います。
スマホサイズについて、表示は横幅375pxで作成し、
デザインデータは2倍の横幅750pxのカンバスサイズで作成してください。
(Retinaディスプレイに対応するため)
レスポンシブウェブデザインを意識したデザインでお願いします。

■サイトマップ
添付の画面遷移図をご確認ください。

■参考サイト
http://hoshizora-tetsuko.co.jp/

■内容について
鋳造部品等を製作する会社のサイトリニューアルになります。
既存サイト
http://www.senbeiseiko.com/kiyora/index.html

■素材写真
画像データについては、フリー素材から流用して
イメージ画像に当て込んでください。
足りない場合は、一旦他のサイトの写真をサンプルとして
入れてください。(サンプルなどの表記をお願いします)
また、購入が必要な写真などを利用した場合、
価格とサイト名を教えてください。

また、Lumera Photosで定期契約をしていますので、
Lumera Photosの画像は使用できます。
デザイン時はカンプ画像をお入れいただきますようお願いします。

■ワイヤーフレーム
https://mock.wirevista.net/view/1a2b3c4d-5e6f-4a7b-8c9d-0e1f2a3b4c5d-8812/?fullscreen
コンテンツの構成としてワイヤーフレームを作成しましたが
必ずしもワイヤーフレームの通りではなくて大丈夫です。
TOPページに配置するコンテンツを見ていただき、デザインは
デザイナーの皆様におまかせしたいと思います。

----------------------------------------------------------------------------
【制作物に対するお願い】

■フォントについて
・無料で使えるフォントで作成をお願いします。
・OSに紐づくフォントの使用は控えていただければと思います (ヒラギノなど)

ページ数
1ページ
希望イメージ
シンプル 複雑
単色 カラフル
暗い 明るい
日常 高級
遊び心 厳粛
未来的 伝統的
女性的 男性的
希望する色
アクセントカラー:茶色、もしくは青色
納品ファイル
• 高解像度JPG (.jpg)
• イラストレーター形式 (.ai)
• フォトショップ形式 (.psd)
補足説明
上記のいずれか1つ(アウトラインありとなしの2つ)と高解像度JPGを納品お願いします。
adobe XDでの納品も可能です。

```html
<!DOCTYPE html>
<html lang="ja">
<head>
<meta charset="UTF-8">
<title>清良伸銅株式会社</title>
<link href="https://fonts.googleapis.com/css2?family=Noto+Sans+JP:wght@400;500;700;900&family=Oswald:wght@400;500&display=swap" rel="stylesheet">
<style>
:root{
  --blue:#1d3f9c;
  --blue-pale:#b9c8e6;
  --ink:#1a1a1a;
  --dark:#141414;
  --grey:#666;
  --line:#d8d8d8;
  --white:#fff;
}
*{margin:0;padding:0;box-sizing:border-box}
html,body{width:1200px;height:2980px;overflow:hidden}
body{position:relative;font-family:"Noto Sans JP",sans-serif;color:var(--ink);background:var(--white);font-size:13px;line-height:1.9}
.abs{position:absolute}
.photo{position:absolute}
.en{font-family:"Oswald",sans-serif;letter-spacing:.08em}
.btn{position:absolute;display:flex;align-items:center;justify-content:space-between;padding:0 22px;font-size:12px;height:40px;letter-spacing:.1em}
.btn svg{width:16px;height:8px}
.btn-blue{background:var(--blue);color:var(--white)}
.btn-white{background:var(--white);color:var(--ink)}
.btn-line{border:1px solid var(--white);color:var(--white)}

/* header / hero */
.hero{left:0;top:0;width:1200px;height:395px;background:linear-gradient(135deg,#2a2520 0%,#6b4a30 40%,#c98a4a 62%,#3a2a20 100%)}
.logo{left:40px;top:20px;color:var(--white);font-weight:700;font-size:20px;letter-spacing:.05em}
.nav{right:40px;top:22px;display:flex;gap:6px}
.nav a{display:block;width:86px;height:34px;line-height:34px;text-align:center;background:rgba(20,20,20,.85);color:var(--white);font-size:12px;text-decoration:none}
.tagline{left:0;top:222px;width:1200px;text-align:center}
.tagline span{display:inline-block;background:rgba(20,20,20,.75);color:var(--white);font-size:26px;font-weight:700;letter-spacing:.12em;padding:8px 34px}

/* about */
.about-photo{left:430px;top:470px;width:690px;height:350px;background:linear-gradient(120deg,#7a4a2a,#d59868 45%,#a0602f 70%,#5a6a80)}
.about-accent{left:1050px;top:770px;width:110px;height:110px;background:var(--blue)}
.about-box{left:140px;top:400px;width:340px;height:400px;background:var(--dark);color:var(--white);padding:40px 36px}
.about-box h2{font-size:22px;font-weight:700;letter-spacing:.1em;margin-bottom:22px}
.about-box .lead{font-size:14px;font-weight:500;line-height:1.8;margin-bottom:18px}
.about-box p{font-size:11px;color:#ccc;line-height:2}

/* section heads */
.big-en{font-family:"Oswald",sans-serif;font-size:78px;font-weight:500;color:var(--blue-pale);letter-spacing:.02em;line-height:1;white-space:nowrap}
.head-jp{font-size:22px;font-weight:700;letter-spacing:.1em}

/* products */
.products-en{left:250px;top:885px}
.products-jp{left:180px;top:935px}
.card{position:absolute;top:990px;width:160px}
.card .thumb{width:160px;height:120px}
.card h3{font-size:12px;font-weight:500;margin:8px 0 4px}
.card p{font-size:10px;color:var(--grey);line-height:1.8}

/* manufacturing */
.mfg-photo{left:0;top:1310px;width:560px;height:300px;background:linear-gradient(150deg,#3a2418,#b8743e 40%,#e0a868 55%,#6b3e22)}
.mfg-en{left:650px;top:1318px;font-size:64px}
.mfg-jp{left:620px;top:1345px}
.mfg-bar{left:1150px;top:1310px;width:50px;height:300px;background:var(--blue)}
.mfg-title{left:620px;top:1400px;font-size:18px;font-weight:700;line-height:1.7;letter-spacing:.05em}
.mfg-text{left:620px;top:1470px;width:480px;font-size:11px;color:var(--grey)}

/* recruit */
.rec-photo{left:180px;top:1705px;width:1020px;height:400px;background:linear-gradient(160deg,#8a5a4a,#b78070 40%,#6a4a40 70%,#3a3030)}
.rec-accent{left:1060px;top:1690px;width:100px;height:110px;background:var(--blue)}
.rec-box{left:180px;top:1705px;width:700px;height:400px;background:rgba(20,20,20,.82);color:var(--white);padding:40px 60px 0 100px}
.rec-box .en{font-size:11px;color:#bbb}
.rec-box .head-jp{font-size:18px;margin-bottom:26px}
.rec-box h3{font-size:18px;font-weight:700;letter-spacing:.08em;margin-bottom:22px;white-space:nowrap}
.rec-box p{font-size:11px;color:#ccc;line-height:2}

/* news */
.news-head{left:0;top:2140px;width:1200px;text-align:center}
.news-head .en{font-size:11px;color:var(--grey)}
.news-list{left:250px;top:2210px;width:700px;list-style:none;border-top:1px solid var(--line)}
.news-list li{display:flex;border-bottom:1px solid var(--line);padding:18px 10px;font-size:11px}
.news-list time{width:120px;flex:none;color:var(--ink)}
.news-list span{color:var(--grey);line-height:1.8}

/* contact */
.contact{left:0;top:2600px;width:1200px;height:250px;background:linear-gradient(120deg,#1a1410,#3a2a1f 40%,#7a4a28 60%,#1a1410)}
.contact-inner{left:0;top:2620px;width:1200px;text-align:center;color:var(--white)}
.contact-inner .en{font-size:11px;color:#ccc}
.contact-inner .head-jp{font-size:18px}
.contact-inner h3{font-size:18px;font-weight:700;letter-spacing:.08em;margin-top:16px}
.contact-inner p{font-size:11px;color:#ccc;margin:10px auto 0;width:560px}
.tel{left:285px;top:2785px;color:var(--white);display:flex;align-items:center;gap:8px}
.tel small{font-size:11px}
.tel b{font-family:"Oswald",sans-serif;font-size:26px;font-weight:500;letter-spacing:.04em}

/* footer */
.f-logo{left:170px;top:2875px;font-size:16px;font-weight:700}
.f-addr{left:170px;top:2903px;font-size:9px;color:var(--grey);line-height:1.7}
.f-nav{left:690px;top:2880px;display:flex;gap:26px;font-size:10px}
.f-copy{left:170px;top:2945px;font-size:9px;color:var(--grey)}
.f-links{left:860px;top:2945px;font-size:9px;color:var(--grey)}
</style>
</head>
<body>

<header>
  <div class="abs hero photo" role="img" aria-label="火花が散る金属加工の現場写真"></div>
  <div class="abs logo">清良伸銅株式会社</div>
  <nav class="abs nav"><a>会社概要</a><a>製品紹介</a><a>製造案内</a><a>採用情報</a><a>お問い合わせ</a></nav>
  <div class="abs tagline"><span>鋳造技術に、自信と誇りを持って</span></div>
</header>

<section class="about">
  <div class="photo about-photo" role="img" aria-label="工場に並ぶ銅コイルの写真"></div>
  <div class="abs about-accent"></div>
  <div class="abs about-box">
    <h2>清良伸銅とは</h2>
    <p class="lead">モノ創りのプロとして、<br>確かな技術でお応えします。</p>
    <p>清良伸銅は創業以来、銅合金の鋳造と加工に一貫して取り組んでまいりました。確かな品質と柔軟な対応で、お客様のものづくりを支えます。</p>
    <p style="margin-top:10px">熟練の技術と最新の設備を組み合わせ、小ロットから量産まで幅広いご要望にお応えいたします。</p>
  </div>
  <div class="btn btn-blue" style="left:176px;top:720px;width:170px">READ MORE<svg viewBox="0 0 16 8"><path d="M0 7h14L9 2" stroke="#fff" fill="none"/></svg></div>
</section>

<section class="products">
  <div class="abs big-en products-en">PRODUCTS</div>
  <div class="abs head-jp products-jp">製品紹介</div>
  <div class="card" style="left:180px"><div class="thumb photo" style="position:static;background:linear-gradient(135deg,#f0ece6,#d9a860)" role="img" aria-label="真鍮製の精密部品の写真"></div><h3>精密部品</h3><p>高い精度が求められる銅合金の小型部品を製作しています。</p></div>
  <div class="card" style="left:520px"><div class="thumb photo" style="position:static;background:linear-gradient(135deg,#f2efe8,#c9a050)" role="img" aria-label="鋳造された真鍮部品の写真"></div><h3>鋳物部品</h3><p>砂型鋳造による複雑な形状の部品にも対応いたします。</p></div>
  <div class="card" style="left:860px"><div class="thumb photo" style="position:static;background:linear-gradient(135deg,#3a3a3a,#b0b4bc 50%,#505560)" role="img" aria-label="金属製品が並ぶ写真"></div><h3>その他の製品</h3><p>ご要望に合わせた各種金属製品の製作も承ります。</p></div>
</section>

<section class="manufacturing">
  <div class="photo mfg-photo" role="img" aria-label="巻かれた銅の帯材のクローズアップ写真"></div>
  <div class="abs big-en mfg-en">MANUFACTURING</div>
  <div class="abs head-jp mfg-jp">製造案内</div>
  <div class="abs mfg-bar"></div>
  <div class="abs mfg-title">充実した設備と確かな技術で<br>お客様のご要望に応えます。</div>
  <p class="abs mfg-text">清良伸銅ではお客様のニーズに合わせた最適な製造方法をご提案いたします。溶解から鋳造、機械加工、検査まで一貫した体制で高品質な製品をお届けします。</p>
  <div class="btn btn-blue" style="left:920px;top:1550px;width:170px">READ MORE<svg viewBox="0 0 16 8"><path d="M0 7h14L9 2" stroke="#fff" fill="none"/></svg></div>
</section>

<section class="recruit">
  <div class="abs rec-accent"></div>
  <div class="photo rec-photo" role="img" aria-label="レンガ造りの工場建物の写真"></div>
  <div class="abs rec-box">
    <div class="en">RECRUIT</div>
    <div class="head-jp">採用情報</div>
    <h3>清良伸銅ではともに働く仲間を募集しています。</h3>
    <p>ものづくりに興味のある方、技術を身につけたい方を歓迎します。未経験の方も先輩社員が丁寧に指導しますので安心してご応募ください。</p>
    <p>私たちと一緒に、次の世代へ技術をつないでいきましょう。</p>
  </div>
  <div class="btn btn-white" style="left:460px;top:2025px;width:170px">募集要項<svg viewBox="0 0 16 8"><path d="M0 7h14L9 2" stroke="#1a1a1a" fill="none"/></svg></div>
  <div class="btn btn-line" style="left:660px;top:2025px;width:170px">エントリー<svg viewBox="0 0 16 8"><path d="M0 7h14L9 2" stroke="#fff" fill="none"/></svg></div>
</section>

<section class="news">
  <div class="abs news-head"><div class="en">NEWS</div><div class="head-jp">お知らせ</div></div>
  <ul class="abs news-list">
    <li><time>2022.11.10</time><span>工場見学の受付を再開いたしました。ご希望の方はお問い合わせフォームより日時をご連絡ください。担当者より折り返しご案内いたします。</span></li>
    <li><time>2022.09.30</time><span>年末年始の休業期間についてお知らせいたします。</span></li>
    <li><time>2022.09.08</time><span>夏季休業のお知らせ 休業期間：8月11日から8月16日まで</span></li>
    <li><time>2022.08.01</time><span>新しい鋳造設備を導入いたしました。これにより大型部品の生産能力が向上し、納期短縮にもつながります。今後ともよろしくお願いいたします。</span></li>
  </ul>
  <div class="btn btn-blue" style="left:515px;top:2500px;width:170px">一覧を見る<svg viewBox="0 0 16 8"><path d="M0 7h14L9 2" stroke="#fff" fill="none"/></svg></div>
</section>

<section class="contact-sec">
  <div class="abs contact photo" role="img" aria-label="暗い工場内で火花が散る写真"></div>
  <div class="abs contact-inner">
    <div class="en">CONTACT</div>
    <div class="head-jp">お問い合わせ</div>
    <h3>ご質問やご相談をお持ちの方は、どうぞお気軽にお問い合わせください。</h3>
    <p>製品や製造に関するご質問、お見積りのご依頼など、お電話またはメールにて承っております。担当者より迅速にご対応いたします。</p>
  </div>
  <div class="abs tel"><svg width="20" height="20" viewBox="0 0 24 24"><path d="M6.6 10.8a15 15 0 0 0 6.6 6.6l2.2-2.2a1 1 0 0 1 1-.25 11.4 11.4 0 0 0 3.6.6 1 1 0 0 1 1 1V20a1 1 0 0 1-1 1A17 17 0 0 1 3 4a1 1 0 0 1 1-1h3.5a1 1 0 0 1 1 1c0 1.25.2 2.45.6 3.6a1 1 0 0 1-.25 1z" fill="#fff"/></svg><small>TEL</small><b>03-4521-7760</b></div>
  <div class="btn btn-blue" style="left:690px;top:2785px;width:230px">メールでのお問い合わせ<svg viewBox="0 0 16 8"><path d="M0 7h14L9 2" stroke="#fff" fill="none"/></svg></div>
</section>

<footer>
  <div class="abs f-logo">清良伸銅株式会社</div>
  <div class="abs f-addr">〒100-0000 東京都千代田区架空町1-2-3<br>TEL 03-4521-7760</div>
  <div class="abs f-nav"><span>会社概要</span><span>製品紹介</span><span>製造案内</span><span>採用情報</span></div>
  <div class="abs f-copy">© Kiyora Shindo Co., Ltd. All Rights Reserved.</div>
  <div class="abs f-links">プライバシーポリシー　サイトマップ</div>
</footer>

</body>
</html>
```